Marlow Air Services E-mail Signature

Need to create an email signature for Marlow Air Services. Signature should include the Marlow logo and the associated TRFC member logo

```html
<!DOCTYPE html>
<html lang="en">
<head>
<meta charset="utf-8">
<title>Marlow Air Services – E-mail Signature</title>
<link rel="stylesheet" href="https://fonts.googleapis.com/css2?family=Montserrat:wght@400;500;600;700&display=swap">
<style>
  :root {
    --page-bg: #e5e6e8;
    --card-bg: #ffffff;
    --brand-blue: #0b62b1;
    --sky-mid: #4f97dc;
    --sky-light: #b7d8f5;
    --ink: #1d1d1f;
    --ink-soft: #3a3a3c;
    --rule: #c9c9c9;
    --white: #ffffff;
  }
  * { box-sizing: border-box; margin: 0; padding: 0; }
  html, body { width: 1089px; height: 1200px; overflow: hidden; }
  body {
    background: var(--page-bg);
    font-family: "Montserrat", Arial, sans-serif;
    color: var(--ink);
    position: relative;
  }
  .sprite { position: absolute; width: 0; height: 0; overflow: hidden; }

  .signature {
    position: absolute;
    left: 78px;
    width: 952px;
    height: 296px;
    background: var(--card-bg);
    overflow: hidden;
  }
  .signature--one { top: 71px; }
  .signature--two { top: 448px; }
  .signature--three { top: 840px; }

  .signature__band {
    position: absolute; left: 0; right: 0; bottom: 0;
    height: 9px; background: var(--brand-blue);
  }
  .signature__sky {
    position: absolute; left: 0; top: 0;
    width: 952px; height: 287px;
  }

  .person {
    position: absolute; right: 51px; top: 38px;
    text-align: right; color: var(--white);
  }
  .person__name { font-weight: 700; font-size: 22px; line-height: 1.2; }
  .person__role { font-weight: 500; font-size: 14px; margin-top: 4px; }

  .brand {
    position: absolute; left: 60px; top: 124px;
    font-weight: 700; font-size: 21px; color: var(--brand-blue);
    letter-spacing: 0.2px;
  }

  .divider {
    position: absolute; left: 297px; top: 130px;
    width: 3px; height: 121px; background: var(--brand-blue);
  }
  .signature--three .divider { top: 127px; height: 60px; width: 2px; background: var(--ink); }

  .address {
    position: absolute; left: 332px; top: 124px;
    font-size: 14px; line-height: 18px; color: var(--ink-soft);
  }
  .address__label { font-weight: 700; color: var(--ink); }
  .address__rule {
    width: 219px; height: 1px; background: var(--rule); margin-top: 8px;
  }

  .contact-list {
    position: absolute; left: 332px; top: 196px;
    list-style: none; font-size: 14px; line-height: 19px; color: var(--ink-soft);
  }

  .contact {
    position: absolute; display: flex; align-items: center; gap: 9px;
    font-size: 14.5px; color: var(--ink-soft); white-space: nowrap;
  }
  .contact svg { width: 24px; height: 24px; flex: none; }
  .signature--three .contact { font-size: 16px; }

  .social {
    position: absolute; display: flex; gap: 13px;
  }
  .social__dot {
    width: 25px; height: 25px; border-radius: 50%;
    background: var(--brand-blue);
  }
  .social--light .social__dot { background: var(--white); }

  .member {
    position: absolute; display: flex; align-items: center; gap: 10px;
  }
  .member__mark {
    width: 30px; height: 30px; border-radius: 50%;
    border: 4px solid var(--brand-blue); flex: none;
  }
  .member__text { position: relative; }
  .member__kicker {
    position: absolute; right: 0; top: -14px;
    font-size: 9px; font-weight: 500; color: var(--ink);
  }
  .member__name {
    font-size: 25px; font-weight: 700; color: var(--ink); letter-spacing: 2px; line-height: 1;
  }
</style>
</head>
<body>

<svg class="sprite" aria-hidden="true">
  <defs>
    <linearGradient id="sky-gradient" x1="1" y1="0" x2="0.35" y2="1">
      <stop offset="0" stop-color="#0b62b1"/>
      <stop offset="0.55" stop-color="#1f70bd"/>
      <stop offset="0.85" stop-color="#4f97dc"/>
      <stop offset="1" stop-color="#b7d8f5"/>
    </linearGradient>
    <symbol id="icon-phone" viewBox="0 0 24 24">
      <circle cx="12" cy="12" r="12" fill="#1d1d1f"/>
      <path fill="#fff" d="M9.2 6.6c.3-.3.8-.3 1 .1l1.1 1.8c.2.3.1.7-.1 1l-.8.7c.6 1.3 1.6 2.3 2.9 2.9l.7-.8c.3-.3.7-.3 1-.1l1.8 1.1c.4.2.4.7.1 1l-1 1c-.5.5-1.2.6-1.8.4-2.9-1-5.1-3.2-6.1-6.1-.2-.6 0-1.3.4-1.8z"/>
    </symbol>
    <symbol id="icon-mail" viewBox="0 0 24 24">
      <circle cx="12" cy="12" r="12" fill="#1d1d1f"/>
      <rect x="6.5" y="8" width="11" height="8" rx="1" fill="#fff"/>
      <path d="M6.8 8.4 12 12.3l5.2-3.9" fill="none" stroke="#1d1d1f" stroke-width="1.2"/>
    </symbol>
    <symbol id="icon-web" viewBox="0 0 24 24">
      <circle cx="12" cy="12" r="12" fill="#1d1d1f"/>
      <g fill="none" stroke="#fff" stroke-width="1.2">
        <circle cx="12" cy="12" r="5.5"/>
        <ellipse cx="12" cy="12" rx="2.4" ry="5.5"/>
        <path d="M6.5 12h11M7.3 9.3h9.4M7.3 14.7h9.4"/>
      </g>
    </symbol>
  </defs>
</svg>

<!-- Signature variant: stacked contact lines -->
<section class="signature signature--one">
  <svg class="signature__sky" viewBox="0 0 952 287" role="img" aria-label="Cloud illustration in blue tones sweeping across the top right">
    <path fill="url(#sky-gradient)" d="M180 0H952V287C900 270 860 220 800 200 720 172 640 150 560 120 460 90 330 80 250 40 215 24 195 10 180 0Z"/>
  </svg>
  <div class="person">
    <p class="person__name">Elena Varga</p>
    <p class="person__role">Marketing Expert</p>
  </div>
  <p class="brand">Marlow Air Services</p>
  <div class="divider"></div>
  <div class="address">
    <p class="address__label">address</p>
    <p>Your Street Address Her</p>
    <p>New Your Sity Aip - 000</p>
    <div class="address__rule"></div>
  </div>
  <ul class="contact-list">
    <li>p : 00 123 456 7890</li>
    <li>e : username@mailbox.com</li>
    <li>w : www.websitename.com</li>
  </ul>
  <div class="social" style="left:63px;top:234px;" aria-label="Social profiles">
    <span class="social__dot"></span><span class="social__dot"></span><span class="social__dot"></span><span class="social__dot"></span>
  </div>
  <div class="member" style="left:737px;top:236px;">
    <span class="member__mark"></span>
    <div class="member__text"><span class="member__kicker">member of</span><p class="member__name">TRFC</p></div>
  </div>
  <div class="signature__band"></div>
</section>

<!-- Signature variant: contact icons -->
<section class="signature signature--two">
  <svg class="signature__sky" viewBox="0 0 952 287" role="img" aria-label="Cloud illustration in blue tones sweeping across the top right">
    <path fill="url(#sky-gradient)" d="M180 0H952V287C900 270 860 220 800 200 720 172 640 150 560 120 460 90 330 80 250 40 215 24 195 10 180 0Z"/>
  </svg>
  <div class="person">
    <p class="person__name">Elena Varga</p>
    <p class="person__role">Marketing Expert</p>
  </div>
  <p class="brand">Marlow Air Services</p>
  <div class="divider"></div>
  <div class="address">
    <p class="address__label">address</p>
    <p>Your Street Address Her</p>
    <p>New Your Sity Aip - 000</p>
    <div class="address__rule"></div>
  </div>
  <p class="contact" style="left:332px;top:209px;"><svg><use href="#icon-phone"/></svg>00 123 456 7890</p>
  <p class="contact" style="left:515px;top:209px;"><svg><use href="#icon-mail"/></svg>username@mailbox.com</p>
  <p class="contact" style="left:332px;top:239px;"><svg><use href="#icon-web"/></svg>www.websitename.com</p>
  <div class="social" style="left:63px;top:234px;" aria-label="Social profiles">
    <span class="social__dot"></span><span class="social__dot"></span><span class="social__dot"></span><span class="social__dot"></span>
  </div>
  <div class="member" style="left:737px;top:236px;">
    <span class="member__mark"></span>
    <div class="member__text"><span class="member__kicker">member of</span><p class="member__name">TRFC</p></div>
  </div>
  <div class="signature__band"></div>
</section>

<!-- Signature variant: single contact row -->
<section class="signature signature--three">
  <svg class="signature__sky" viewBox="0 0 952 287" role="img" aria-label="Cloud illustration in blue tones sweeping across the top right">
    <path fill="url(#sky-gradient)" d="M180 0H952V287C900 270 860 220 800 200 720 172 640 150 560 120 460 90 330 80 250 40 215 24 195 10 180 0Z"/>
  </svg>
  <div class="person">
    <p class="person__name">Elena Varga</p>
    <p class="person__role">Marketing Expert</p>
  </div>
  <div class="social social--light" style="left:766px;top:116px;" aria-label="Social profiles">
    <span class="social__dot"></span><span class="social__dot"></span><span class="social__dot"></span><span class="social__dot"></span>
  </div>
  <p class="brand" style="top:120px;">Marlow Air Services</p>
  <div class="divider"></div>
  <div class="address" style="top:120px;">
    <p class="address__label">address</p>
    <p>Your Street Address Her</p>
    <p>New Your Sity Aip - 000</p>
    <div class="address__rule"></div>
  </div>
  <p class="contact" style="left:61px;top:240px;"><svg><use href="#icon-phone"/></svg>00 123 456 7890</p>
  <p class="contact" style="left:244px;top:240px;"><svg><use href="#icon-mail"/></svg>username@mailbox.com</p>
  <p class="contact" style="left:483px;top:240px;"><svg><use href="#icon-web"/></svg>www.websitename.com</p>
  <div class="member" style="left:768px;top:237px;">
    <span class="member__mark"></span>
    <div class="member__text"><p class="member__name">TRFC</p></div>
  </div>
  <div class="signature__band"></div>
</section>

</body>
</html>
```